TallyForge needs a new rocket based website

We need a new website that will be based on our rocket ship logo. We develop innovative solutions for enterprises. We would like to see a design that when the pages scroll, the rocket launches and goes from launch through a journey, similar to how we approach our customer. We would like areas for "Who are we", "What can we do", "What have we done", "How can we help". http://www.tallyforge.com.au is our current website

Target Market(s)

Government, Enterprise, Cloud

Industry/Entity Type

Software Service

Coding

Coded - Design and coding required

Number of Pages Required

2 page

Requirements
Must have
• We would like to see a design that when the pages scroll, the rocket launches and goes from launch through a journey, similar to how we approach our customer.
• Must have a home page and a detail page.
• Would like to see the logo/rocket animate in some way when you scroll through he page.

```html
<!DOCTYPE html>
<html lang="en">
<head>
<meta charset="utf-8">
<title>TallyForge: Innovative Software Solutions</title>
<link rel="stylesheet" href="https://fonts.googleapis.com/css2?family=Tinos:wght@400;700&display=swap">
<style>
  :root {
    --orange: #ffa500;
    --orange-deep: #f08a00;
    --ink: #000;
    --line: #bdbdbd;
    --footer: #808080;
    --white: #fff;
    --link: #1a0dab;
    --social: #3b5998;
  }
  * { box-sizing: border-box; margin: 0; padding: 0; }
  html, body { width: 679px; height: 1200px; overflow: hidden; }
  body { font-family: "Tinos", "Times New Roman", serif; color: var(--ink); background: var(--white); position: relative; font-size: 11px; }

  .site-header { height: 56px; display: flex; align-items: center; justify-content: center; gap: 6px; }
  .brand { font-weight: 700; font-size: 22px; color: var(--orange-deep); }
  .brand-dot { width: 14px; height: 14px; border-radius: 50%; background: var(--orange-deep); }

  .hero { margin: 0 10px; height: 249px; background: var(--orange); display: flex; flex-direction: column; align-items: center; overflow: hidden; }
  .hero-rocket { margin-top: 16px; width: 30px; height: 148px; border-radius: 15px; background: linear-gradient(180deg, #2b2b2b, #e06a00 70%, var(--orange)); animation: launch 3s ease-in-out infinite alternate; }
  @keyframes launch {
    from { transform: translateY(6px); }
    to { transform: translateY(-6px); }
  }
  .hero-title { margin-top: 14px; font-size: 17px; font-weight: 700; text-align: center; line-height: 1.25; }

  .about { text-align: center; }
  .about h1 { margin-top: 20px; font-size: 27px; font-weight: 700; }
  .about-brand { margin: 18px auto 0; height: 96px; display: flex; align-items: center; justify-content: center; gap: 8px; }
  .about-brand .brand-dot { width: 40px; height: 40px; }
  .about-brand .brand { font-size: 24px; }
  .about p { margin-top: 14px; line-height: 1.3; }

  .panel { margin: 0 10px; border: 1px solid var(--line); padding: 16px 12px; }
  .panel h2 { font-size: 18px; font-weight: 700; }
  .panel hr { border: 0; border-top: 1px solid #8a8a8a; margin: 14px 0 16px; }
  .services { margin-top: 12px; height: 288px; }
  .service h3 { font-size: 11px; font-weight: 700; margin-bottom: 13px; }
  .service p { margin-bottom: 17px; }
  .customers { margin-top: 4px; height: 160px; padding-top: 22px; }
  .customers ul { list-style: none; line-height: 1.25; }
  .customers a { color: var(--link); }

  .site-footer { position: absolute; left: 10px; right: 10px; top: 983px; bottom: 8px; background: var(--footer); color: var(--white); padding: 8px 12px; }
  .site-footer h4 { font-size: 12px; font-weight: 700; margin-bottom: 14px; }
  .contact-form label { display: block; }
  .contact-form input, .contact-form textarea { display: block; width: 96px; border: 1px solid #555; background: var(--white); font: inherit; font-size: 9px; }
  .contact-form input { height: 14px; }
  .contact-form textarea { height: 32px; resize: none; }
  .contact-form button { margin-top: 5px; font: inherit; font-size: 10px; padding: 0 4px; background: #eee; border: 1px solid #555; }
  .mail-icon { display: block; margin-top: 5px; }
  address { font-style: normal; margin-top: 6px; line-height: 1.25; }
  .phone { margin-top: 10px; }
  .social { position: absolute; left: 50%; top: 160px; width: 22px; height: 22px; margin-left: -11px; border-radius: 50%; background: var(--social); }
  .copyright { position: absolute; left: 0; right: 0; top: 186px; text-align: center; }
  .copyright a { color: #3b3bd6; }
</style>
</head>
<body>
  <header class="site-header">
    <span class="brand-dot"></span><span class="brand">TallyForge</span>
  </header>

  <section class="hero">
    <div class="hero-rocket" role="img" aria-label="Rocket launching upward with flame trail"></div>
    <h2 class="hero-title">TallyForge:<br>Innovative Software Solutions</h2>
  </section>

  <section class="about">
    <h1>WHO ARE WE?</h1>
    <div class="about-brand"><span class="brand-dot"></span><span class="brand">TallyForge</span></div>
    <p>Offering the latest in enterprise architecture, design and development of bespoke software solutions<br>Always researching and implementing the latest technology for customers.</p>
  </section>

  <section class="panel services">
    <h2>Our Services</h2>
    <hr>
    <div class="service"><h3>e-Parliament</h3><p>All of your Parliamentary software and business process needs.</p></div>
    <div class="service"><h3>Cloud</h3><p>Cloud Office Suites, Migration, Security, Customisations.</p></div>
    <div class="service"><h3>Architecture and Design</h3><p>Business process design, technology strategy and architecture.</p></div>
    <div class="service"><h3>Software Development</h3><p>Software development including business apps, web and mobile.</p></div>
  </section>

  <section class="panel customers">
    <h2>Our Customers</h2>
    <hr>
    <ul>
      <li><a href="#">Assembly of Westmark</a></li>
      <li><a href="#">Assembly of New Southland Isles</a></li>
      <li><a href="#">Office of the Premier and Council</a></li>
    </ul>
  </section>

  <footer class="site-footer">
    <h4>Contact us</h4>
    <form class="contact-form">
      <label for="email">Your email</label>
      <input id="email" type="text" placeholder="email...">
      <label for="message">Message:</label>
      <textarea id="message"></textarea>
      <button type="button">Send</button>
    </form>
    <svg class="mail-icon" width="10" height="10" viewBox="0 0 10 10" aria-hidden="true">
      <path d="M2 1h4l2 2v6H2z" fill="#fff" stroke="#333" stroke-width="0.8"/>
    </svg>
    <address>Unit 4, 118 Larkspur Rd<br>Elmbrook, SA 5190</address>
    <p class="phone">(08) 8123 456</p>
    <span class="social" role="img" aria-label="Social profile link"></span>
    <p class="copyright">© 2018 <a href="http://www.tallyforge.com.au">TallyForge.com</a> All rights Reserved.</p>
  </footer>
</body>
</html>
```